Banner Design for Physiotherapy Business

I need a banner designed for a physiotherapy business. The word ‘Physiotherapy’ should be prominent at the top. I’ve attached a document outlining what text and a suggestion of a picture I’d like included. The photo I have suggested in the document won’t upload to plumvista though as the dimensions are too large. I am open to other photos being used though. I would like to see designs that use the colour orange (as seen in the example) or green preferrably. The dimensions need to be 841mm x 2055mm and provided in PDF, JPG, and PNG format and 300dpi in CMYK colour mode.

```html
<!DOCTYPE html>
<html lang="en">
<head>
<meta charset="utf-8">
<title>Physiotherapy Banner</title>
<link href="https://fonts.googleapis.com/css2?family=Oswald:wght@500&family=PT+Sans:wght@400;700&display=swap" rel="stylesheet">
<style>
  :root {
    --orange: #e8731f;
    --orange-light: #f28c28;
    --orange-deep: #dd6420;
    --teal: #7fd1bb;
    --teal-dark: #5fbfa6;
    --navy: #1f2a4d;
    --text: #2b2b3a;
    --white: #ffffff;
    --page: #ececec;
    --panel: #f4f5f6;
  }
  * { box-sizing: border-box; margin: 0; padding: 0; }
  html, body { width: 1200px; height: 1014px; overflow: hidden; }
  body { background: var(--page); font-family: "PT Sans", sans-serif; }

  .banner {
    position: absolute; left: 403px; top: 27px;
    width: 393px; height: 960px;
    background: var(--panel);
    overflow: hidden;
    box-shadow: 0 2px 10px rgba(0,0,0,.12);
  }

  .header {
    position: absolute; left: 0; top: 0; width: 100%; height: 170px;
  }
  .header svg { position: absolute; inset: 0; }
  .title {
    position: absolute; left: 0; right: 0; top: 36px;
    text-align: center; color: var(--white);
    font-family: "Oswald", sans-serif; font-weight: 500;
    font-size: 50px; letter-spacing: 3px; line-height: 1;
  }

  .hero-photo {
    position: absolute; left: 0; top: 150px; width: 100%; height: 400px;
    background: linear-gradient(100deg, #e9e6e2 0%, #f3ece8 35%, #f1c9c4 55%, #eef1ef 75%, #dfeee8 100%);
    z-index: 0;
  }
  .header { z-index: 2; }

  .photo-edge { position: absolute; left: 0; top: 490px; width: 100%; height: 90px; z-index: 2; }

  .member-badge {
    position: absolute; left: 258px; top: 548px; z-index: 3;
    width: 34px; height: 26px; border-radius: 50%;
    background: #2a8fd0;
  }

  .services { position: absolute; left: 0; top: 588px; width: 100%; z-index: 3; }
  .services-title {
    text-align: center; color: var(--orange);
    font-weight: 700; font-size: 21px; letter-spacing: .2px;
  }
  .service-columns {
    display: flex; gap: 14px; padding: 0 18px 0 20px; margin-top: 18px;
  }
  .service-list { list-style: none; flex: 1; }
  .service-list li {
    position: relative; padding-left: 11px;
    font-size: 10.5px; line-height: 1.12; color: var(--text);
    min-height: 23.5px;
  }
  .service-list li::before {
    content: ""; position: absolute; left: 0; top: 3px;
    width: 5px; height: 5px; border-radius: 50%;
    background: var(--orange);
  }

  .appointment {
    position: absolute; left: 0; top: 826px; width: 100%; z-index: 3;
    text-align: center;
  }
  .appointment-label { color: var(--navy); font-weight: 700; font-size: 13px; }
  .phone-pill {
    display: inline-flex; align-items: center; gap: 10px;
    margin-top: 6px; height: 32px; padding: 0 26px;
    background: var(--teal); border-radius: 10px;
    color: var(--white); font-weight: 700; font-size: 17px;
    box-shadow: 0 3px 4px rgba(0,0,0,.15);
  }

  .footer { position: absolute; left: 0; top: 868px; width: 100%; height: 92px; z-index: 2; }
  .footer svg { position: absolute; inset: 0; }
  .footer-text {
    position: absolute; left: 0; right: 0; top: 30px;
    text-align: center; color: var(--white); font-size: 12.5px; line-height: 1.9;
  }
  .footer-text .web { font-size: 14px; }
</style>
</head>
<body>
  <main class="banner">
    <header class="header">
      <svg viewBox="0 0 393 170" preserveAspectRatio="none">
        <defs>
          <linearGradient id="headerFill" x1="0" x2="1">
            <stop offset="0" stop-color="var(--orange-deep)"/>
            <stop offset="1" stop-color="var(--orange-light)"/>
          </linearGradient>
        </defs>
        <path d="M0 0H393V152C300 142 200 162 110 158C60 156 25 150 0 146Z" fill="url(#headerFill)"/>
        <path d="M0 148C25 152 60 158 110 160C200 164 300 146 393 154" fill="none" stroke="var(--white)" stroke-width="5"/>
        <path d="M0 153C25 157 60 163 110 165C200 169 300 151 393 159" fill="none" stroke="var(--teal)" stroke-width="3"/>
      </svg>
      <h1 class="title">PHYSIOTHERAPY</h1>
    </header>

    <div class="hero-photo" role="img" aria-label="Photo: physiotherapist supporting an older woman's shoulders as she stretches a teal resistance band"></div>

    <svg class="photo-edge" viewBox="0 0 393 90" preserveAspectRatio="none">
      <path d="M0 40C70 62 150 64 230 44C300 26 350 20 393 24V90H0Z" fill="var(--panel)"/>
      <path d="M0 38C60 56 140 58 220 40C290 24 345 16 393 20V26C345 24 290 32 220 50C140 70 60 70 0 56Z" fill="var(--orange)"/>
      <path d="M0 58C60 72 140 72 220 52C290 34 345 26 393 28" fill="none" stroke="var(--teal)" stroke-width="2"/>
    </svg>

    <div class="member-badge" aria-hidden="true"></div>

    <section class="services">
      <h2 class="services-title">WHAT WE TREAT / SERVICES</h2>
      <div class="service-columns">
        <ul class="service-list">
          <li>Arthritis</li>
          <li>Back pain / Neck pain</li>
          <li>Sciatic pain</li>
          <li>Sports injuries</li>
          <li>Repetitive strain injuries</li>
          <li>Shoulder pain and dysfunction</li>
          <li>Post surgical management (hip and knee arthroscopes, joint replacement surgery)</li>
        </ul>
        <ul class="service-list">
          <li>Tennis elbow</li>
          <li>Postural pain</li>
          <li>Workplace injuries</li>
          <li>Motor vehicle accidents</li>
          <li>Women's health issues</li>
          <li>Clinical exercise</li>
          <li>Pre-employment functional assessments</li>
        </ul>
      </div>
    </section>

    <section class="appointment">
      <p class="appointment-label">MAKE AN APPOINTMENT</p>
      <div class="phone-pill">
        <svg width="16" height="16" viewBox="0 0 16 16" aria-hidden="true">
          <circle cx="8" cy="8" r="7" fill="none" stroke="var(--white)" stroke-width="1.4"/>
          <path d="M5.4 4.4l1.2-.2.7 1.8-.8.7c.4.9 1 1.5 1.9 1.9l.7-.8 1.8.7-.2 1.2c-.1.4-.5.6-.9.6C7.2 10.1 5.9 8.8 5.6 5.3c0-.4.2-.8.6-.9z" fill="var(--white)"/>
        </svg>
        <span>(03) 9000 4812</span>
      </div>
    </section>

    <footer class="footer">
      <svg viewBox="0 0 393 92" preserveAspectRatio="none">
        <path d="M0 8C120 0 260 2 393 14" fill="none" stroke="var(--teal)" stroke-width="2"/>
        <path d="M0 14C120 6 260 8 393 20V92H0Z" fill="var(--orange)"/>
      </svg>
      <div class="footer-text">
        <p>Elmbrook Family Practice: 18-20 Harlow St Elmbrook VIC 3999</p>
        <p class="web">www.elmbrookfamilypractice.com.au</p>
      </div>
    </footer>
  </main>
</body>
</html>
```